Poster to promote Global Critter Care Fest

Hi Designers,

Animal lovers all over the world are grateful for the work of vets.

To recognize all their efforts, Global Critter Care Fest takes place globally on April 30. This year's theme is 'Continuing education with a one health focus'.

It's about working alongside the human health sector to tackle animal disease and food safety. Read more here: http://www.brenvalu.org/for-the-media/press-releases/detail/article/global-critter-care-fest-award-2016/

We want you to design a poster to promote the day, and the key message.

The poster must feature:
- the words 'Global Critter Care Fest'
- the date 'April 30, 2016'
- the theme 'Continuing education with a one health focus

You can choose any imagery and colors you feel will be engaging for the audience and will reflect the industry and messages.

Think animal, vets, pets, caring, health.

Looking forward to seeing your ideas.

Thanks

PixelHive

• - the words 'Global Critter Care Fest'
• - the date 'April 30, 2016'
• - the theme 'Continuing education with a one health focus

```html
<!DOCTYPE html>
<html lang="en">
<head>
<meta charset="utf-8">
<title>Global Critter Care Fest – Poster</title>
<link href="https://fonts.googleapis.com/css2?family=Open+Sans:wght@400;600&display=swap" rel="stylesheet">
<style>
  :root {
    --lime: #8cc63e;
    --lime-light: #d6e125;
    --berry: #e03f55;
    --paper: #ffffff;
    --mist: #ededed;
    --mist-dark: #d9d9d9;
    --ink-soft: #6b6b6b;
    --ink-olive: #3a3f1a;
    --photo-grass-light: #b3c98a;
    --photo-grass: #8aa85a;
    --photo-lawn-light: #78a043;
    --photo-lawn: #55802e;
  }
  html, body {
    margin: 0;
    padding: 0;
    overflow: hidden;
    background: var(--paper);
  }
  .poster {
    position: relative;
    width: 970px;
    height: 1200px;
    overflow: hidden;
    font-family: "Open Sans", Arial, sans-serif;
    background: var(--paper);
  }
  .poster__backdrop {
    position: absolute;
    inset: 0;
  }
  .poster__title {
    position: absolute;
    left: 26px;
    top: 40px;
    margin: 0;
    font-weight: 600;
    line-height: 1.0;
    letter-spacing: 1px;
  }
  .poster__title span { display: block; }
  .title-light {
    color: var(--paper);
    font-weight: 400;
    font-size: 82px;
  }
  .title-accent {
    color: var(--berry);
    font-size: 88px;
  }
  .title-bold {
    color: var(--paper);
    font-size: 88px;
  }
  .poster__date {
    position: absolute;
    left: 30px;
    top: 330px;
    margin: 0;
    font-size: 26px;
    font-weight: 600;
    color: var(--ink-olive);
  }
  .photo-frame {
    position: absolute;
    border-radius: 50%;
    background: var(--paper);
    box-shadow: 0 6px 22px rgba(0, 0, 0, 0.22);
  }
  .photo-frame--main {
    left: 221px;
    top: 380px;
    width: 500px;
    height: 500px;
  }
  .photo-frame--small {
    left: 519px;
    top: 675px;
    width: 300px;
    height: 300px;
  }
  .photo-frame__image {
    position: absolute;
    inset: 22px;
    border-radius: 50%;
  }
  .photo-frame--main .photo-frame__image {
    background: linear-gradient(180deg, var(--photo-grass-light) 0%, var(--photo-grass) 100%);
  }
  .photo-frame--small .photo-frame__image {
    inset: 20px;
    background: linear-gradient(180deg, var(--photo-lawn-light) 0%, var(--photo-lawn) 100%);
  }
  .poster__theme {
    position: absolute;
    left: 0;
    right: 0;
    top: 1012px;
    margin: 0;
    text-align: center;
    color: var(--berry);
    font-weight: 400;
    line-height: 1.15;
  }
  .theme-lead { display: block; font-size: 38px; }
  .theme-tail { display: block; font-size: 28px; }
  .poster__body {
    position: absolute;
    left: 50px;
    right: 50px;
    top: 1108px;
    margin: 0;
    text-align: center;
    font-size: 17px;
    line-height: 1.7;
    color: var(--ink-soft);
  }
</style>
</head>
<body>
<main class="poster">
  <svg class="poster__backdrop" width="970" height="1200" viewBox="0 0 970 1200" aria-hidden="true">
    <defs>
      <linearGradient id="lime-wash" x1="0" y1="0" x2="0.3" y2="1">
        <stop offset="0" stop-color="#8cc63e" />
        <stop offset="0.6" stop-color="#d6e125" />
        <stop offset="1" stop-color="#b8d22a" />
      </linearGradient>
      <linearGradient id="mist-wash" x1="0" y1="0" x2="1" y2="1">
        <stop offset="0" stop-color="#d9d9d9" />
        <stop offset="0.55" stop-color="#f6f6f6" />
        <stop offset="1" stop-color="#ededed" />
      </linearGradient>
    </defs>
    <rect width="970" height="1200" fill="url(#mist-wash)" role="img" aria-label="Faded photo of a vet with a stethoscope and a happy dog" />
    <polygon points="0,0 970,0 970,173 0,604" fill="url(#lime-wash)" role="img" aria-label="Faded photo of a cat under a lime green wash" />
    <polygon points="0,604 970,173 970,313 0,818" fill="#e03f55" />
  </svg>

  <h1 class="poster__title">
    <span class="title-light">GLOBAL</span>
    <span class="title-accent">CRITTER CARE</span>
    <span class="title-bold">FEST</span>
  </h1>
  <p class="poster__date">April 30, 2016</p>

  <div class="photo-frame photo-frame--main">
    <div class="photo-frame__image" role="img" aria-label="Photo of two children meeting a ginger kitten on the grass"></div>
  </div>
  <div class="photo-frame photo-frame--small">
    <div class="photo-frame__image" role="img" aria-label="Photo of a child stroking a brown dog on the lawn"></div>
  </div>

  <h2 class="poster__theme">
    <span class="theme-lead">Continuing education with</span>
    <span class="theme-tail">a one health focus</span>
  </h2>
  <p class="poster__body">To celebrate the Global Critter Care Fest (GCCF) that will take place globally on 30 April 2016, the Global Vet Alliance (GVA) and the Brenvalu Animal Health Council</p>
</main>
</body>
</html>
```